Marla's Bake biz card

Home made customized gourmet cakes

Contact Information for Business Card

Launching a cake business called

"Marla's Bakes"
Gourmet Cakes with a smile
(555) 284-9160 marlaquent@bakemailbox.test
Picture of one cake
phone number
email address
FB page

back would pictures of 4 cakes

I can submit pictures later

Font styles to use
Serif

Requirements
Must have
• One picture on the front, four pictures on the back.
• Warm and inviting look.
• Bee Hive cake goes on the front of the card.

```html
<!DOCTYPE html>
<html lang="en">
<head>
<meta charset="utf-8">
<title>Marla's Bakes – Business Card</title>
<link href="https://fonts.googleapis.com/css2?family=Merriweather:wght@700;900&display=swap" rel="stylesheet">
<style>
  :root {
    --bg: #e8e3dc;
    --ink: #111111;
    --paper: #ffffff;
    --honey: #f7a21b;
    --honey-light: #ffd84a;
    --honey-deep: #e07a10;
    --shadow: rgba(0,0,0,0.18);
  }
  * { margin: 0; padding: 0; box-sizing: border-box; }
  html, body {
    width: 1200px; height: 1000px; overflow: hidden;
    background: var(--bg);
    font-family: "Merriweather", Georgia, serif;
    color: var(--ink);
  }
  .canvas { position: relative; width: 1200px; height: 1000px; }

  /* Front of card */
  .card-front {
    position: absolute; left: 110px; top: 110px;
    width: 360px; height: 620px;
    background: var(--ink);
    padding: 14px;
    box-shadow: 0 8px 24px var(--shadow);
  }
  .card-front__frame {
    width: 100%; height: 100%;
    background: var(--paper);
    padding: 6px;
  }
  .card-front__photo {
    position: relative; width: 100%; height: 100%;
    background: radial-gradient(ellipse at 45% 40%, var(--honey-light) 0%, #f9c52a 40%, var(--honey) 75%, var(--honey-deep) 100%);
    overflow: hidden;
  }
  .logo {
    font-weight: 900; color: var(--ink); line-height: 0.95;
  }
  .card-front .logo {
    position: absolute; left: 40px; top: 190px;
    font-size: 58px;
  }
  .card-front .logo .logo__second { display: block; padding-left: 20px; }
  .tagline {
    position: absolute; left: 18px; right: 18px; top: 440px;
    border-top: 2px solid var(--ink);
    border-bottom: 2px solid var(--ink);
    padding: 12px 0 14px;
    text-align: center;
    font-weight: 700; font-size: 22px; line-height: 1.25;
  }

  /* Back of card */
  .card-back {
    position: absolute; left: 520px; top: 330px;
    width: 620px; height: 360px;
    box-shadow: 0 8px 24px var(--shadow);
  }
  .card-back svg { display: block; }
  .card-back .logo-text { font-family: "Merriweather", Georgia, serif; font-weight: 900; fill: var(--ink); }
  .card-back .contact-text { font-family: "Merriweather", Georgia, serif; font-weight: 700; fill: var(--ink); font-size: 14px; }
</style>
</head>
<body>
<main class="canvas">

  <section class="card-front" aria-label="Business card front">
    <div class="card-front__frame">
      <div class="card-front__photo" role="img" aria-label="Photo of a honeycomb beehive cake decorated with small fondant bees">
        <div class="logo"><span>Marla's</span><span class="logo__second">Bakes</span></div>
        <p class="tagline">Gourmet Cakes<br>with a smile</p>
      </div>
    </div>
  </section>

  <section class="card-back" aria-label="Business card back">
    <svg width="620" height="360" viewBox="0 0 620 360" xmlns="http://www.w3.org/2000/svg">
      <defs>
        <clipPath id="gallery-clip">
          <polygon points="0,0 218,0 334,190 258,360 0,360"/>
        </clipPath>
        <linearGradient id="cake-floral" x1="0" y1="0" x2="1" y2="1">
          <stop offset="0" stop-color="#e84a8a"/><stop offset="0.5" stop-color="#f5e9e0"/><stop offset="1" stop-color="#27a9a8"/>
        </linearGradient>
        <linearGradient id="cake-blooms" x1="0" y1="0" x2="1" y2="1">
          <stop offset="0" stop-color="#c8202c"/><stop offset="0.5" stop-color="#f0a020"/><stop offset="1" stop-color="#efe8dc"/>
        </linearGradient>
        <linearGradient id="cake-cactus" x1="0" y1="0" x2="1" y2="1">
          <stop offset="0" stop-color="#5a9a3a"/><stop offset="1" stop-color="#6b4a2a"/>
        </linearGradient>
        <linearGradient id="cake-chocolate" x1="0" y1="0" x2="1" y2="1">
          <stop offset="0" stop-color="#4a2412"/><stop offset="0.6" stop-color="#2e160a"/><stop offset="1" stop-color="#e86a9a"/>
        </linearGradient>
      </defs>

      <rect class="back-panel" width="620" height="360" fill="var(--honey)"/>
      <polygon class="back-band" points="0,0 250,0 370,190 290,360 0,360" fill="var(--ink)"/>
      <polyline class="back-divider" points="234,0 352,190 274,360" fill="none" stroke="var(--paper)" stroke-width="5"/>

      <g class="gallery" clip-path="url(#gallery-clip)">
        <g transform="rotate(-32 170 180)">
          <rect x="15" y="25" width="150" height="150" fill="url(#cake-floral)" role="img" aria-label="Photo of a cake topped with bright sugar flowers"/>
          <rect x="175" y="25" width="150" height="150" fill="url(#cake-blooms)" role="img" aria-label="Photo of a cake with piped buttercream roses and sunflowers"/>
          <rect x="15" y="185" width="150" height="150" fill="url(#cake-cactus)" role="img" aria-label="Photo of a cake decorated with piped cactus plants"/>
          <rect x="175" y="185" width="150" height="150" fill="url(#cake-chocolate)" role="img" aria-label="Photo of a chocolate cake with fondant pigs in a mud pool"/>
        </g>
      </g>

      <text class="logo-text" x="575" y="82" font-size="42" text-anchor="end">Marla's</text>
      <text class="logo-text" x="575" y="130" font-size="42" text-anchor="end">Bakes</text>

      <g class="contact">
        <text class="contact-text" x="574" y="256" text-anchor="end">(555) 284-9160</text>
        <g class="icon-phone" transform="translate(584 244)" fill="var(--ink)">
          <path d="M2 4 C2 1 14 1 14 4 L12 6 L10 5 L10 4 C8 3.4 8 3.4 6 4 L6 5 L4 6 Z"/>
          <rect x="4" y="7" width="8" height="6" rx="1"/>
        </g>

        <text class="contact-text" x="574" y="288" text-anchor="end" textLength="212" lengthAdjust="spacingAndGlyphs">marlaquent@bakemailbox.test</text>
        <g class="icon-mail" transform="translate(584 277)">
          <rect x="0" y="0" width="15" height="11" fill="var(--ink)"/>
          <polyline points="1,1 7.5,6.5 14,1" fill="none" stroke="var(--honey)" stroke-width="1.4"/>
        </g>

        <text class="contact-text" x="574" y="320" text-anchor="end">marlaquent</text>
        <rect class="icon-social" x="584" y="308" width="14" height="14" fill="var(--ink)"/>
      </g>
    </svg>
  </section>

</main>
</body>
</html>
```